Heritage Hollow Business Cards

Require a business card design. <br/><br/>Needs to include logo (either round or long version) plus these details:<br/>Maya Torvel<br/>Heritage Hollow<br/>maya@quonbrook.com.au<br/>02 6481 7390<br/>PO Box Glenwarra NSW 2913<br/>www.heritagehollow.com.au<br/><br/>I need in an editable format so that I can create for multiple staff members. <br/><br/>

Target Market(s)

We are an online store selling renovation products to home owners are builders. Looking for a classic classy design.

Industry/Entity Type

Home And Garden

Contact Information for Business Card

Maya Torvel
Heritage Hollow
maya@quonbrook.com.au
02 6481 7390
PO Box Glenwarra NSW 2913
www.heritagehollow.com.au

Colors

Designer to choose colors to be used in the design.

Requirements
Must have
• Must include Logo.

```html
<!DOCTYPE html>
<html lang="en">
<head>
<meta charset="utf-8">
<title>Heritage Hollow Business Cards</title>
<link href="https://fonts.googleapis.com/css2?family=Arvo:wght@400;700&display=swap" rel="stylesheet">
<style>
  :root {
    --bg: #8c8c8c;
    --green: #4f6f5f;
    --paper: #ffffff;
    --ink: #6b6b6b;
    --ink-dark: #5a5a5a;
    --chalk: #e9ece8;
    --rule: #8a8a8a;
  }
  * { margin: 0; padding: 0; box-sizing: border-box; }
  html, body { width: 1200px; height: 965px; overflow: hidden; }
  body {
    background: var(--bg);
    font-family: "Arvo", Georgia, serif;
    position: relative;
  }
  .card {
    position: absolute;
    left: 278px;
    width: 648px;
    height: 368px;
    border-radius: 24px;
  }
  .card--front { top: 98px; background: var(--green); }
  .card--back { top: 504px; background: var(--paper); }

  .brand-mark {
    position: absolute;
    border-radius: 50%;
    display: flex;
    align-items: center;
    justify-content: center;
    text-align: center;
    font-weight: 400;
    line-height: 1.1;
  }
  .card--front .brand-mark {
    left: 222px; top: 80px;
    width: 216px; height: 216px;
    border: 1.5px solid var(--chalk);
    color: var(--chalk);
    font-size: 28px;
    padding-top: 60px;
  }
  .card--back .brand-mark {
    left: 78px; top: 90px;
    width: 196px; height: 196px;
    border: 1.5px solid var(--rule);
    color: var(--ink-dark);
    font-size: 26px;
    padding-top: 56px;
  }
  .website {
    position: absolute;
    left: 0; right: 0; top: 322px;
    text-align: center;
    color: var(--chalk);
    font-weight: 700;
    font-size: 16px;
    letter-spacing: 0.5px;
  }
  .tagline {
    position: absolute;
    left: 33px; top: 310px;
    color: var(--ink);
    font-weight: 700;
    font-size: 13.5px;
    letter-spacing: 0.3px;
  }
  .details {
    position: absolute;
    left: 324px; top: 96px;
    color: var(--ink);
  }
  .details__name {
    font-size: 22px;
    font-weight: 700;
    letter-spacing: 1.5px;
    color: var(--ink-dark);
    margin-bottom: 24px;
  }
  .details__address {
    font-style: normal;
    font-weight: 700;
    font-size: 15.5px;
    line-height: 21px;
    margin-bottom: 16px;
  }
  .contact-line {
    display: flex;
    align-items: center;
    gap: 9px;
    font-weight: 700;
    font-size: 15.5px;
    line-height: 23px;
  }
  .contact-line svg { width: 16px; height: 14px; fill: var(--ink); flex: none; }
</style>
</head>
<body>
  <section class="card card--front" aria-label="Card front">
    <div class="brand-mark">Heritage<br>Hollow</div>
    <p class="website">www.heritagehollow.com.au</p>
  </section>

  <section class="card card--back" aria-label="Card back">
    <div class="brand-mark">Heritage<br>Hollow</div>
    <p class="tagline">Buy Traditional Hardware Online</p>
    <div class="details">
      <h1 class="details__name">MAYA TORVEL</h1>
      <address class="details__address">
        Heritage Hollow<br>
        PO Box Glenwarra<br>
        NSW 2913 Australia
      </address>
      <p class="contact-line">
        <svg viewBox="0 0 16 16" aria-hidden="true"><path d="M3.6 1.2l2.3 2.6-1.2 1.9c.9 2 2.5 3.6 4.5 4.5l1.9-1.2 2.6 2.3-1.3 2.5C7.2 13.4 2.6 8.8 1.2 2.6z"/></svg>
        02 6481 7390
      </p>
      <p class="contact-line">
        <svg viewBox="0 0 16 12" aria-hidden="true"><path d="M0 0h16v1.2L8 6.6 0 1.2z M0 2.6l8 5.4 8-5.4V12H0z"/></svg>
        maya@quonbrook.com.au
      </p>
    </div>
  </section>
</body>
</html>
```